CORVEN HIDEWORKS COLLECTIVE BUSINESS CARD
BUSINESS CARD
CORVEN HIDEWORKS COLLECTIVE BUSINESS CARD -
Creative Brief
Use specific fonts
Anything professional
Professional
Hal Durnsey
CEO
512 Wexbury Lane Manhasset, NY 11284, USA
hdurnsey@corvenhideworks.com
www.corvenhideworks.com
Please add "Alliance of Pelmora Hide Finishers" under our logo.

```html
<!DOCTYPE html>
<html lang="en">
<head>
<meta charset="utf-8">
<title>Corven Hideworks Collective Stationery</title>
<link rel="stylesheet" href="https://fonts.googleapis.com/css2?family=Cinzel:wght@600&family=Montserrat:wght@400;600&display=swap">
<style>
:root{
  --bg:#2b2c2d;
  --bg-dark:#1e1f20;
  --green:#3f8d2b;
  --green-dark:#1f4f19;
  --green-light:#7cc04a;
  --paper:#ffffff;
  --paper-shade:#eef0ee;
  --ink:#3a3a3a;
  --ink-soft:#8a8a8a;
  --faint:#e4e8e3;
}
*{margin:0;padding:0;box-sizing:border-box}
html,body{width:1200px;height:348px;overflow:hidden}
body{background:radial-gradient(ellipse at 50% 45%,var(--bg) 0%,var(--bg-dark) 100%);font-family:"Montserrat",sans-serif;position:relative;color:var(--ink)}
.brand{display:flex;align-items:center;gap:4px;font-family:"Cinzel",serif;font-weight:600;color:var(--green);white-space:nowrap}
.brand-mark{background:var(--green);display:inline-block}
.identity{position:absolute;left:10px;top:22px;width:134px;text-align:center}
.identity .brand{justify-content:center;flex-direction:column;gap:3px;font-size:7.4px;color:var(--paper)}
.identity .brand-mark{width:26px;height:26px}
.identity .rule{height:1px;background:var(--ink-soft);margin:4px 8px}
.identity .tagline{font-size:5.3px;color:#c9c9c9}
.identity .tagline.green{color:var(--green-light);margin-top:3px}
.sheet{position:absolute;background:var(--paper);box-shadow:0 2px 6px rgba(0,0,0,.5)}
.card{left:8px;top:100px;width:136px;height:70px;padding:8px}
.card .brand{font-size:4.6px}
.card .brand-mark{width:10px;height:10px}
.card .details{position:absolute;left:8px;bottom:8px;font-size:4.3px;line-height:1.4}
.card .name{font-weight:600;font-size:5.2px;color:var(--green-dark)}
.letterhead{top:24px;width:188px;height:305px}
.lh-a{left:193px}.lh-b{left:401px}
.letterhead .brand{position:absolute;left:50%;top:14px;transform:translateX(-50%);font-size:5px;flex-direction:column}
.letterhead .brand-mark{width:16px;height:16px}
.contact{position:absolute;right:12px;top:14px;font-size:3.6px;line-height:1.5;color:var(--ink-soft)}
.faint-name{position:absolute;left:0;right:0;top:118px;text-align:center;font-family:"Cinzel",serif;font-weight:600;font-size:15px;line-height:1.3;color:var(--faint)}
.footer{position:absolute;left:0;right:0;bottom:9px;text-align:center;font-size:3.6px;color:var(--ink-soft)}
.slip{left:638px;width:207px;height:84px}
.slip-a{top:137px}.slip-b{top:233px}
.slip .brand{position:absolute;left:12px;top:10px;font-size:4.6px}
.slip .brand-mark{width:10px;height:10px}
.slip .contact{top:10px}
.slip .faint-name{top:28px;font-size:9px}
.slip .footer{bottom:6px}
.envelope{left:890px;width:290px;height:72px;overflow:hidden}
.env-black{top:126px;background:#141414}
.env-green{top:178px;left:900px;transform:rotate(-3deg);background:linear-gradient(180deg,var(--green-light),var(--green) 55%,var(--green-dark))}
.env-white{top:246px;height:74px}
.envelope svg{position:absolute;inset:0}
.envelope .brand{position:absolute;left:16px;top:10px;font-size:4.6px;color:var(--paper)}
.envelope .brand-mark{width:10px;height:10px;background:var(--paper)}
.env-white .brand{color:var(--green)}
.env-white .brand-mark{background:var(--green)}
.return{position:absolute;left:16px;top:24px;font-size:3.6px;line-height:1.5;color:var(--ink-soft)}
</style>
</head>
<body>
<section class="identity">
  <div class="brand"><span class="brand-mark"></span>CORVEN HIDEWORKS COLLECTIVE</div>
  <div class="rule"></div>
  <p class="tagline">Alliance of Pelmora Hide Finishers</p>
  <p class="tagline green">Hal Durnsey · CEO</p>
</section>

<article class="sheet card">
  <div class="brand"><span class="brand-mark"></span>CORVEN HIDEWORKS COLLECTIVE</div>
  <div class="details">
    <p class="name">Hal Durnsey</p>
    <p>CEO</p>
    <p>512 Wexbury Lane Manhasset, NY 11284, USA</p>
    <p>T 516 555 0142</p>
    <p>hdurnsey@corvenhideworks.com</p>
    <p>www.corvenhideworks.com</p>
  </div>
</article>

<article class="sheet letterhead lh-a">
  <div class="brand"><span class="brand-mark"></span>CORVEN HIDEWORKS COLLECTIVE</div>
  <div class="contact"><p>512 Wexbury Lane</p><p>Manhasset, NY 11284, USA</p><p>T 516 555 0142</p><p>hdurnsey@corvenhideworks.com</p></div>
  <p class="faint-name">CORVEN<br>HIDEWORKS<br>COLLECTIVE</p>
  <p class="footer">www.corvenhideworks.com</p>
</article>

<article class="sheet letterhead lh-b">
  <p class="faint-name">CORVEN<br>HIDEWORKS<br>COLLECTIVE</p>
  <p class="footer">512 Wexbury Lane Manhasset, NY 11284, USA · www.corvenhideworks.com</p>
</article>

<article class="sheet slip slip-a">
  <div class="brand"><span class="brand-mark"></span>CORVEN HIDEWORKS COLLECTIVE</div>
  <div class="contact"><p>512 Wexbury Lane</p><p>Manhasset, NY 11284, USA</p><p>F 516 555 0143</p></div>
  <p class="faint-name">CORVEN HIDEWORKS</p>
</article>

<article class="sheet slip slip-b">
  <p class="faint-name">CORVEN HIDEWORKS</p>
  <p class="footer">512 Wexbury Lane Manhasset, NY 11284, USA · www.corvenhideworks.com</p>
</article>

<article class="sheet envelope env-black">
  <svg viewBox="0 0 290 72" preserveAspectRatio="none"><path d="M0 52 Q145 24 290 52 L290 72 L0 72Z" fill="var(--green)"/></svg>
  <div class="brand"><span class="brand-mark"></span>CORVEN HIDEWORKS COLLECTIVE</div>
</article>

<article class="sheet envelope env-green">
  <svg viewBox="0 0 290 72" preserveAspectRatio="none"><path d="M0 0 L290 0 L290 18 Q145 46 0 18Z" fill="var(--paper)"/></svg>
</article>

<article class="sheet envelope env-white">
  <div class="brand"><span class="brand-mark"></span>CORVEN HIDEWORKS COLLECTIVE</div>
  <div class="return"><p>512 Wexbury Lane</p><p>Manhasset, NY 11284, USA</p></div>
</article>
</body>
</html>
```